Vellacourt Winery Wine Label Re-design

Vellacourt Winery is located in the Finger Lakes region of New York. The Calloway Family planted the first vineyards in 1979 and opened in 1986. We produce award winning premium, hand crafted estate grown wines. We are in the process of a wine label re-design across our entire line. We would like to have the new label 'pop' but still convey elegance and ultra-premium quality. We are open to all color and styles or a minimalist design.
The attached files contain our new logo and samples of our current label (marked current) with dimensions. Our labeler is limited to label shapes but does not necessarily to have to be die-cut(the top arch) like our current label.

Target Market(s)

Upper income quality wine drinkers

Colors

Designer to choose colors to be used in the design.

Requirements
Should not have
• Should not be a tranparent label

```html
<!DOCTYPE html>
<html lang="en">
<head>
<meta charset="utf-8">
<title>Vellacourt Winery – Cabernet Sauvignon Label</title>
<link rel="stylesheet" href="https://fonts.googleapis.com/css2?family=Cinzel:wght@400;500&family=Libre+Baskerville&family=Montserrat:wght@300;400&display=swap">
<style>
  :root {
    --backdrop: #f4ede2;
    --label-paper: #ffffff;
    --gold: #c6ae2c;
    --maroon: #4b1f30;
    --band-text: #fdfbf2;
  }
  * { margin: 0; padding: 0; box-sizing: border-box; }
  html, body {
    width: 1200px;
    height: 1000px;
    overflow: hidden;
    background: var(--backdrop);
  }
  .canvas {
    width: 1200px;
    height: 1000px;
    display: flex;
    align-items: center;
    justify-content: center;
  }
  .wine-label { width: 560px; height: 780px; display: block; }
  .label-shape { fill: var(--label-paper); stroke: var(--maroon); stroke-width: 7; }
  .label-inner-edge { fill: none; stroke: var(--gold); stroke-width: 4; }
  .header-band { fill: var(--gold); }
  .header-rule { fill: none; stroke: var(--maroon); stroke-width: 2; }
  .header-rule-light { fill: none; stroke: var(--band-text); stroke-width: 1.5; }
  .brand-name {
    font-family: "Cinzel", serif;
    font-size: 46px;
    letter-spacing: 7px;
    fill: var(--band-text);
  }
  .brand-sub {
    font-family: "Montserrat", sans-serif;
    font-weight: 300;
    font-size: 20px;
    letter-spacing: 9px;
    fill: var(--band-text);
  }
  .varietal-panel { fill: var(--label-paper); stroke: var(--gold); stroke-width: 4; }
  .varietal-panel-inner { fill: none; stroke: var(--gold); stroke-width: 1.5; }
  .varietal-name {
    font-family: "Libre Baskerville", serif;
    font-size: 31px;
    fill: var(--maroon);
  }
  .vintage-year {
    font-family: "Libre Baskerville", serif;
    font-size: 19px;
    fill: var(--gold);
  }
  .ornament-area { fill: var(--maroon); }
  .wave-band { fill: none; stroke: var(--gold); stroke-width: 6; }
  .wave-band-thin { fill: none; stroke: var(--maroon); stroke-width: 2; }
  .seal-ring { fill: var(--label-paper); stroke: var(--maroon); stroke-width: 3; }
  .seal-name {
    font-family: "Libre Baskerville", serif;
    font-size: 19px;
    fill: var(--maroon);
  }
</style>
</head>
<body>
<main class="canvas">
  <svg class="wine-label" viewBox="0 0 560 780" xmlns="http://www.w3.org/2000/svg" aria-label="Vellacourt Winery Cabernet Sauvignon 2018 label">
    <path class="label-shape" d="M4,4 H556 V560 Q556,600 505,630 L335,742 Q280,778 225,742 L55,630 Q4,600 4,560 Z"/>
    <path class="label-inner-edge" d="M22,22 H538 V552 Q538,590 492,618 L326,724 Q280,754 234,724 L68,618 Q22,590 22,552 Z"/>

    <rect class="header-band" x="22" y="22" width="516" height="180"/>
    <rect class="header-rule" x="14" y="14" width="532" height="4"/>
    <polyline class="header-rule-light" points="48,70 48,40 512,40 512,70"/>
    <text class="brand-name" x="283" y="116" text-anchor="middle">VELLACOURT</text>
    <text class="brand-sub" x="284" y="156" text-anchor="middle">WINERY</text>

    <path class="varietal-panel" d="M44,180 H516 V360 Q470,372 420,360 Q350,344 280,352 Q210,344 140,360 Q90,372 44,360 Z"/>
    <path class="varietal-panel-inner" d="M58,194 H502 V346 Q462,356 420,346 Q350,330 280,338 Q210,330 140,346 Q98,356 58,346 Z"/>
    <text class="varietal-name" x="280" y="262" text-anchor="middle">CABERNET SAUVIGNON</text>
    <rect class="ornament-area" x="168" y="294" width="50" height="10" rx="5" role="img" aria-label="small flourish ornament"/>
    <text class="vintage-year" x="280" y="306" text-anchor="middle">2018</text>
    <rect class="ornament-area" x="342" y="294" width="50" height="10" rx="5" role="img" aria-label="small flourish ornament"/>

    <path class="wave-band" d="M22,392 Q100,372 170,388 Q230,400 280,392 Q330,400 390,388 Q460,372 538,392"/>
    <path class="wave-band-thin" d="M22,410 Q100,390 170,406 Q230,418 280,410 Q330,418 390,406 Q460,390 538,410"/>

    <rect class="ornament-area" x="60" y="468" width="130" height="24" rx="12" role="img" aria-label="scroll flourish ornament"/>
    <rect class="ornament-area" x="370" y="468" width="130" height="24" rx="12" role="img" aria-label="scroll flourish ornament"/>
    <circle class="seal-ring" cx="280" cy="520" r="64"/>
    <text class="seal-name" x="280" y="527" text-anchor="middle">Vellacourt</text>
  </svg>
</main>
</body>
</html>
```